Business card design for new brand

We have recently rebranded and need a new business card template.

We are an insurance underwriting agency. All of our products are sold via other partner companies, so these are just to pass on our details to other organisations.

We would like to see designs that use the colour green (current stationary generally uses lime green (rgb 142,190,63) and forest green (0,154,79) to comply with our logo's colours. We are happy with other shades of green.

Business cards need to include our logo, as well as space for:
1. Full name
2. Qualifications (optional)
3. Title
4. Office number
5. Mobile number
6. Email address

Our logo is enclosed here.

```html
<!DOCTYPE html>
<html lang="en">
<head>
<meta charset="utf-8">
<title>Fernway Cover – Business Card</title>
<link rel="stylesheet" href="https://fonts.googleapis.com/css2?family=Barlow:wght@400;500;700&display=swap">
<style>
  :root {
    --backdrop: #c9c9c9;
    --card-white: #ffffff;
    --card-black: #1c1c1c;
    --ink: #111111;
    --forest: #00893a;
    --forest-dark: #03561f;
    --lime: #8ebe3f;
    --chartreuse: #d4d800;
    --silver: #9a9a9a;
  }
  * { box-sizing: border-box; margin: 0; padding: 0; }
  html, body { width: 1200px; height: 800px; overflow: hidden; }
  body {
    background: var(--backdrop);
    font-family: "Barlow", Arial, sans-serif;
    position: relative;
  }
  .card {
    position: absolute;
    top: 250px;
    width: 525px;
    height: 300px;
    box-shadow: 0 6px 18px rgba(0,0,0,0.18);
  }
  .card--front { left: 60px; background: var(--card-white); }
  .card--back { left: 615px; background: var(--card-black); }

  .contact {
    position: absolute;
    top: 34px;
    right: 34px;
    text-align: right;
    color: var(--ink);
  }
  .contact__name {
    font-weight: 700;
    font-size: 24px;
    letter-spacing: 0.5px;
    line-height: 1;
  }
  .contact__title {
    color: var(--forest);
    font-size: 15px;
    margin: 3px 0 10px;
  }
  .contact__list { list-style: none; }
  .contact__item {
    display: flex;
    justify-content: flex-end;
    align-items: center;
    gap: 8px;
    font-size: 14px;
    line-height: 20px;
  }
  .contact__item svg { width: 12px; height: 12px; flex: none; }

  .brand-mark {
    position: absolute;
    display: flex;
    align-items: center;
    gap: 14px;
    font-weight: 500;
  }
  .brand-mark__square { flex: none; }
  .card--front .brand-mark { left: 40px; bottom: 40px; color: var(--forest); font-size: 40px; }
  .card--front .brand-mark__square { width: 46px; height: 46px; background: var(--lime); }
  .card--back .brand-mark { left: 60px; top: 108px; color: var(--silver); font-size: 34px; line-height: 1.05; }
  .card--back .brand-mark__square { width: 56px; height: 56px; background: var(--forest); }
  .brand-mark__sub { display: block; font-size: 34px; }
</style>
</head>
<body>
  <section class="card card--front">
    <div class="contact">
      <p class="contact__name">DANIEL HART</p>
      <p class="contact__title">President</p>
      <ul class="contact__list">
        <li class="contact__item">412-380-7741
          <svg viewBox="0 0 12 12" aria-hidden="true"><path d="M2 1h3l1 3-2 1a7 7 0 0 0 3 3l1-2 3 1v3c-6 0-10-4-10-9z" fill="var(--forest-dark)"/></svg>
        </li>
        <li class="contact__item">412-903-2268
          <svg viewBox="0 0 12 12" aria-hidden="true"><rect x="3" y="0.8" width="6" height="10.4" rx="1" fill="none" stroke="var(--forest)" stroke-width="1.4"/></svg>
        </li>
        <li class="contact__item">hello@fernwaycover.com
          <svg viewBox="0 0 12 12" aria-hidden="true"><rect x="0.5" y="2" width="11" height="8" fill="var(--lime)"/><path d="M1 2.5l5 4 5-4" fill="none" stroke="#fff" stroke-width="1"/></svg>
        </li>
        <li class="contact__item">fernwaycover.com
          <svg viewBox="0 0 12 12" aria-hidden="true"><circle cx="6" cy="6" r="5.5" fill="var(--chartreuse)"/><path d="M0.5 6h11M6 0.5c-3 3-3 8 0 11M6 0.5c3 3 3 8 0 11" fill="none" stroke="#fff" stroke-width="0.8"/></svg>
        </li>
      </ul>
    </div>
    <div class="brand-mark">
      <span class="brand-mark__square"></span>
      <span>Fernway Cover</span>
    </div>
  </section>

  <section class="card card--back">
    <div class="brand-mark">
      <span class="brand-mark__square"></span>
      <span>Fernway Cover<span class="brand-mark__sub">Australia Pty Ltd</span></span>
    </div>
  </section>
</body>
</html>
```